Redesign our company's business card. HSG BUSINESS CARD 2015

We are an Audio Visual Production company with a flare of marketing and sales. Lights camera ACTION!! We are Production and creative designers and thinkers whom provide first class service for many vantage 300 companies that Exhibit at trade shows and sales meetings.

Double sided, sleek, fashionable, and modern.

www.halvernstudio.com

Think ZNQ'S Crestline

Target Market(s)

Trade Show Mangers, Event coordinators, Project managers,

Industry/Entity Type

Marketing

Contact Information for Business Card

Name Tile, Logo, Slogan, photos of our work on the back. Chatterly and blipper

Font styles to use
Sans Serif
Decorative
Script

Colors
33a6d7
ffffff
0692cd
cee9f5

Requirements
Must have
• Multi color, professional, Upscale,
• CREATING GREAT PARTNERSHIPS THAT PRODUCE AMAZING RESULTS
Nice to have
• Photos of our work on the back
Should not have
• Address or fax.

```html
<!DOCTYPE html>
<html lang="en">
<head>
<meta charset="utf-8">
<title>HSG Business Card</title>
<link href="https://fonts.googleapis.com/css2?family=Open+Sans:wght@400;700&display=swap" rel="stylesheet">
<style>
  :root{
    --page:#e9eaec;
    --ink:#1d1d1f;
    --muted:#3c3c40;
    --blue:#0692cd;
    --blue-deep:#0a5f9a;
    --blue-light:#33a6d7;
    --blue-pale:#cee9f5;
    --white:#ffffff;
    --stage-dark:#0b0d14;
    --stage-glow:#1f6fc4;
  }
  *{margin:0;padding:0;box-sizing:border-box}
  html,body{width:1200px;height:852px;overflow:hidden}
  body{background:var(--page);font-family:"Open Sans",Arial,sans-serif;color:var(--ink);position:relative}
  .card{position:absolute;top:276px;width:520px;height:300px;border-radius:22px;overflow:hidden;box-shadow:0 6px 18px rgba(0,0,0,.18)}
  .card--front{left:50px}
  .card--back{left:630px;background:var(--white)}

  .stage-photo{position:absolute;inset:0;
    background:radial-gradient(ellipse 60% 55% at 50% 45%,var(--stage-glow) 0%,#123b73 45%,var(--stage-dark) 100%)}
  .front-logo{position:absolute;left:150px;top:112px;display:flex;align-items:center;gap:16px}
  .logo-dot{width:60px;height:60px;border-radius:50%;background:var(--blue-light);flex:none}
  .logo-name{color:var(--white);font-weight:700;line-height:1}
  .logo-name__mark{display:block;font-size:46px;letter-spacing:3px}
  .logo-name__full{display:block;font-size:12px;letter-spacing:1.5px;margin-top:4px;text-transform:uppercase}

  .back-band{position:absolute;left:0;top:0;bottom:0;width:38px;background:var(--blue-deep);border-right:5px solid var(--ink)}
  .back-logo{position:absolute;left:62px;top:40px;display:flex;align-items:center;gap:14px}
  .back-logo .logo-name{color:var(--blue)}
  .back-logo .logo-dot{width:54px;height:54px}
  .rule{position:absolute;left:250px;right:0;top:136px;height:2px;background:var(--blue-deep)}
  .person{position:absolute;left:62px;top:122px}
  .person__name{font-size:19px;font-weight:700}
  .person__title{font-size:12px;color:var(--muted)}
  .contacts{position:absolute;left:62px;top:178px;list-style:none;font-size:13px;line-height:19px;color:var(--ink)}
  .contacts li{display:flex;align-items:center;gap:10px}
  .contacts svg{width:13px;height:13px;flex:none;fill:var(--blue-deep)}
</style>
</head>
<body>
  <section class="card card--front">
    <div class="stage-photo" role="img" aria-label="Photo of a lit event stage with blue video wall panels and a dark audience hall"></div>
    <div class="front-logo">
      <span class="logo-dot"></span>
      <span class="logo-name"><span class="logo-name__mark">HSG</span><span class="logo-name__full">Halvern Studio Group</span></span>
    </div>
  </section>

  <section class="card card--back">
    <div class="back-band"></div>
    <div class="back-logo">
      <span class="logo-dot"></span>
      <span class="logo-name"><span class="logo-name__mark">HSG</span><span class="logo-name__full">Halvern Studio Group</span></span>
    </div>
    <div class="rule"></div>
    <div class="person">
      <p class="person__name">Your Long Name</p>
      <p class="person__title">Managing Director</p>
    </div>
    <ul class="contacts">
      <li><svg viewBox="0 0 16 16"><path d="M3 1h3l1 4-2 1a9 9 0 0 0 5 5l1-2 4 1v3a2 2 0 0 1-2 2A13 13 0 0 1 1 3a2 2 0 0 1 2-2z"/></svg>555-014-2297</li>
      <li><svg viewBox="0 0 16 16"><path d="M1 3h14v10H1z M1 3l7 6 7-6" stroke="#fff" stroke-width="1.2"/></svg>yourname@halvernstudio.com</li>
      <li><svg viewBox="0 0 16 16"><circle cx="8" cy="8" r="7"/><path d="M1 8h14M8 1v14" stroke="#fff" stroke-width="1"/></svg>www.halvernstudio.com</li>
      <li><svg viewBox="0 0 16 16"><circle cx="8" cy="8" r="7"/></svg>hsgstudio</li>
      <li><svg viewBox="0 0 16 16"><circle cx="8" cy="8" r="7"/></svg>company/halvern-studio-group</li>
      <li><svg viewBox="0 0 16 16"><circle cx="8" cy="8" r="7"/></svg>Halvern-Studio-Group-HSG/50012847361</li>
    </ul>
  </section>
</body>
</html>
```